Digital Billboard Design: Winter Sales Event

I own a boutique furniture store in Calgary, AB (maplewoven.ca) and I am looking to advertise our winter sale event on a new curved digital billboard (specs attached including required file type).

I have this billboard rented for 52-weeks so I will be looking to change the design every 4-weeks (i.e. this is intended to be an ongoing project).

The objective of this first billboard is to raise awareness around our annual winter sales event. The store itself is only a few blocks from the billboard so those commuting into downtown are just a short drive from the store.

I am looking for a fresh, clean, contemporary look that will grab your attention as you drive into downtown Calgary without presenting to much info so as to be distracting (and overwhelming -- the billboard does not need to contain all info on my current marketing material). I should also note that the store caters to a higher-end, more sophisticated clientele so the graphics need to reflect the brand (i.e. we are not Brenton Furniture or Couch Depot!).

I have attached three files:

Billboard specs
Current marketing material advertising sale (and all relevant data)
An idea that is from an American furniture store that I think is interesting

Target Market(s)

Upper middle class, sophisticated client who appreciates the finer things in life.

Industry/Entity Type

Furniture Store

Font styles to use
Sans Serif

Requirements
Must have
• Company Logo
• Winter Sales Event - 20 to 60% off
• Address: 3847 22nd Ave SW
Nice to have
• Image of furniture -- see our website www.maplewoven.ca -- any photo from this site can be used
Should not have
• Too much text or visual distration

```html
<!DOCTYPE html>
<html lang="en">
<head>
<meta charset="utf-8">
<title>Maple Woven – Winter Sales Event Billboards</title>
<link rel="stylesheet" href="https://fonts.googleapis.com/css2?family=Montserrat:wght@300;400&display=swap">
<style>
  :root {
    --page: #ffffff;
    --frame: #3a3a3a;
    --ink: #ffffff;
    --ink-soft: rgba(255,255,255,0.92);
    --teal-grey: #6d8283;
    --slate: #587072;
    --olive: #5b6a52;
    --deep: #4a5c5a;
    --mist: #8fa1a0;
  }
  * { box-sizing: border-box; margin: 0; padding: 0; }
  html, body {
    width: 1200px; height: 1000px; overflow: hidden;
    background: var(--page);
    font-family: "Montserrat", sans-serif;
    color: var(--ink);
  }
  .presentation-board {
    position: relative; width: 1200px; height: 1000px;
  }
  .board-frame {
    position: absolute; left: 33px; top: 35px; width: 1136px; height: 936px;
    border: 3px solid var(--frame);
  }
  .billboard {
    position: absolute; left: 163px; width: 875px; overflow: hidden;
  }
  .billboard--dated { top: 72px; height: 407px; }
  .billboard--event { top: 504px; height: 429px; }
  .billboard__backdrop {
    position: absolute; inset: 0;
    background:
      radial-gradient(circle at 30% 30%, rgba(160,178,178,0.45) 0 60px, transparent 120px),
      radial-gradient(circle at 62% 68%, rgba(120,160,170,0.45) 0 50px, transparent 110px),
      radial-gradient(circle at 85% 25%, rgba(140,155,150,0.5) 0 70px, transparent 150px),
      radial-gradient(ellipse at 10% 85%, var(--olive) 0, transparent 55%),
      radial-gradient(ellipse at 75% 95%, var(--deep) 0, transparent 50%),
      linear-gradient(160deg, var(--teal-grey) 0%, var(--slate) 55%, #5d7170 100%);
    filter: blur(2px);
  }
  .text {
    position: absolute; left: 0; width: 100%;
    text-align: center; line-height: 1; white-space: nowrap;
  }
  .brand-name {
    top: 44px; font-size: 29px; font-weight: 400; letter-spacing: 5px;
  }
  .store-address {
    top: 83px; font-size: 27px; font-weight: 300;
  }
  .offer { position: absolute; left: 30px; width: 380px; }
  .offer__lead, .offer__tail { font-size: 52px; font-weight: 300; }
  .offer__figure { font-size: 86px; font-weight: 400; letter-spacing: -1px; }
  .divider {
    position: absolute; left: 432px; width: 2px; background: var(--ink-soft);
  }
  .headline { position: absolute; left: 450px; width: 405px; }
  .light { font-weight: 300; }
  .regular { font-weight: 400; }
  .event-line { font-size: 34px; }
  .sale-ends { font-size: 36px; font-weight: 300; }
  .end-date { font-size: 74px; font-weight: 400; }
  .end-date small { font-size: 54px; }
  .winter-sales { font-size: 47px; font-weight: 300; }
  .winter-sales .regular { font-weight: 400; }
  .event-big { font-size: 104px; font-weight: 400; letter-spacing: -1px; }
  .footer-line { font-size: 31px; font-weight: 300; }
</style>
</head>
<body>
<main class="presentation-board">
  <div class="board-frame"></div>

  <section class="billboard billboard--dated">
    <div class="billboard__backdrop" role="img" aria-label="Soft blurred interior photo with teal and olive bokeh"></div>
    <div class="text brand-name">MAPLE WOVEN</div>
    <div class="text store-address">3847 22ND AVE SW, CALGARY, AB</div>

    <div class="offer">
      <div class="text offer__lead" style="top:158px">GET</div>
      <div class="text offer__figure" style="top:209px">20-60%</div>
      <div class="text offer__tail" style="top:292px">OFF</div>
    </div>
    <div class="divider" style="top:161px;height:182px"></div>
    <div class="headline">
      <div class="text event-line" style="top:164px"><span class="regular">WINTER</span> <span class="light">SALES</span> <span class="regular">EVENT</span></div>
      <div class="text sale-ends" style="top:226px">SALE ENDS</div>
      <div class="text end-date" style="top:266px">JAN. 31<small>ST</small></div>
    </div>
  </section>

  <section class="billboard billboard--event">
    <div class="billboard__backdrop" role="img" aria-label="Soft blurred interior photo with teal and olive bokeh"></div>
    <div class="text brand-name">MAPLE WOVEN</div>
    <div class="text store-address">3847 22ND AVE SW, CALGARY, AB</div>

    <div class="offer">
      <div class="text offer__lead" style="top:140px">GET</div>
      <div class="text offer__figure" style="top:193px">20-60%</div>
      <div class="text offer__tail" style="top:276px">OFF</div>
    </div>
    <div class="divider" style="top:144px;height:190px"></div>
    <div class="headline">
      <div class="text winter-sales" style="top:168px"><span class="regular">WINTER</span> SALES</div>
      <div class="text event-big" style="top:212px">EVENT</div>
    </div>
    <div class="text footer-line" style="top:366px">SALE ENDS <span class="regular">JANUARY 31ST</span></div>
  </section>
</main>
</body>
</html>
```